Corvana Wound Care Business card design

We need a business card designed around our logo which was provided. The logo of preference is the colored. Also the colors and fonts were provided.

Target Market(s)

Our Referral partners are home health agencies.

Industry/Entity Type

Healthcare

Contact Information for Business Card

Name , Phone #, Email , Title

Requirements
Nice to have
• Creativity
Should not have
• basic

```html
<!DOCTYPE html>
<html lang="en">
<head>
<meta charset="utf-8">
<title>Corvana Wound Care – Business Card</title>
<link rel="stylesheet" href="https://fonts.googleapis.com/css2?family=Montserrat:wght@400;500;700&display=swap">
<style>
  :root {
    --backdrop: #3b3b3e;
    --card: #ffffff;
    --navy: #1f4c93;
    --deep-blue: #2a3fa8;
    --sky: #1e9ad6;
    --ink: #1d1d24;
  }
  * { margin: 0; padding: 0; box-sizing: border-box; }
  html, body {
    width: 1200px; height: 915px; overflow: hidden;
    background: var(--backdrop);
    font-family: "Montserrat", sans-serif;
  }
  .card {
    position: absolute;
    width: 680px; height: 389px;
    background: var(--card);
    border-radius: 22px;
    box-shadow: 0 10px 28px rgba(0,0,0,.45);
  }
  .card--front { left: 120px; top: 50px; }
  .card--back  { left: 400px; top: 476px; }

  .brand {
    display: flex; align-items: center; gap: 18px;
    position: absolute;
  }
  .brand__mark {
    background: linear-gradient(135deg, var(--sky), var(--deep-blue));
    border-radius: 10px;
  }
  .brand__name {
    font-weight: 700; color: var(--navy); line-height: 1.05;
    letter-spacing: .01em;
  }
  .card--front .brand { left: 110px; top: 150px; }
  .card--front .brand__mark { width: 78px; height: 78px; }
  .card--front .brand__name { font-size: 40px; }

  .card--back .brand { left: 48px; top: 162px; gap: 12px; }
  .card--back .brand__mark { width: 44px; height: 44px; border-radius: 7px; }
  .card--back .brand__name { font-size: 22px; }

  .divider {
    position: absolute; left: 330px; top: 60px;
    width: 1.5px; height: 270px; background: var(--navy);
  }
  .contact {
    position: absolute; left: 360px; top: 66px; right: 30px;
    color: var(--ink);
  }
  .contact__name {
    font-weight: 700; font-size: 30px; letter-spacing: .02em;
    background: linear-gradient(90deg, var(--sky), var(--navy));
    -webkit-background-clip: text; background-clip: text; color: transparent;
  }
  .contact__title { font-size: 16px; margin: 4px 0 22px 6px; }
  .contact__row {
    display: flex; align-items: flex-start; gap: 10px;
    font-size: 16px; line-height: 1.3; margin-bottom: 9px;
  }
  .contact__row svg { flex: none; width: 16px; height: 16px; margin-top: 2px; fill: var(--navy); }
  .contact__row--address { margin-bottom: 16px; }
</style>
</head>
<body>
  <section class="card card--front" aria-label="Card front">
    <div class="brand">
      <span class="brand__mark"></span>
      <span class="brand__name">Corvana<br>Wound Care</span>
    </div>
  </section>

  <section class="card card--back" aria-label="Card back">
    <div class="brand">
      <span class="brand__mark"></span>
      <span class="brand__name">Corvana<br>Wound Care</span>
    </div>
    <div class="divider"></div>
    <div class="contact">
      <p class="contact__name">DANA WHITLOW</p>
      <p class="contact__title">Managing Director</p>
      <p class="contact__row contact__row--address">
        <svg viewBox="0 0 16 16"><path d="M8 0a5.5 5.5 0 0 0-5.5 5.5C2.5 10 8 16 8 16s5.5-6 5.5-10.5A5.5 5.5 0 0 0 8 0zm0 8a2.5 2.5 0 1 1 0-5 2.5 2.5 0 0 1 0 5z"/></svg>
        <span>Your address, City<br>State, Zip 1234</span>
      </p>
      <p class="contact__row">
        <svg viewBox="0 0 16 16"><path d="M3.6 1l2.5 3-1.5 1.8c.9 2 2.6 3.7 4.6 4.6L11 8.9l3 2.5-1.2 2.8C7.3 14.5 1.5 8.7 1.8 3.2z"/></svg>
        <span>123 456 789</span>
      </p>
      <p class="contact__row">
        <svg viewBox="0 0 16 16"><path d="M1 3h14v10H1zm1.4 1L8 8.6 13.6 4z"/></svg>
        <span>info@yourgmail.com</span>
      </p>
      <p class="contact__row">
        <svg viewBox="0 0 16 16"><circle cx="8" cy="8" r="7"/></svg>
        <span>www.yourwebsite.com</span>
      </p>
    </div>
  </section>
</body>
</html>
```